Business Card Design Project (Beer industry)

I am seeking a redesign of my business card. I am looking for something that will really stand out in both texture and feel. Something more on the modern side then traditional. Nothing die cut shaped like a beer mug please.

The card is used mostly for other industry professionals, as well as bar and restaurant owners. My title is Strategy & Acquisitions. If you would like to somehow incorporate that theme, that may work.

My business is craft and imported beer. Nothing fizzy and yellow, so my products are more on the upscale side.
Updates

I was able to update my logo in .ai and .tif format. I hope that helps. 

Thank you all for your creative ideas. I have uploaded my current business card in pdf format, as well as our logo in .eps file format. We are excited about the submissions so far and want to thank you all again.

PS Please do not include fax number in future submissions, as we are looking for something more creative and a fax says 1999 and not 2015, which is the message we are going for, without being futuristic. 

Thank you all once again for all of your submissions. If we would consider a two sided card, we would like the opposite side not to be the same as the front. The styles we have seen so far, it appears the front and back are too similar. Again, a two sided card is not required. Thank you and we look forward to pushing the boundaries of your creativity. Cheers

Target Market(s)

My card would mostly go to bar and restaurant operators as well as other beer industry professionals

Industry/Entity Type

Restaurant

Requirements
Nice to have
• Two sided would be considered, although not required
Should not have
• Anything die cut shaped like a beer mug.

```html
<!DOCTYPE html>
<html lang="en">
<head>
<meta charset="utf-8">
<title>Kestrel Beer – Business Card</title>
<link rel="stylesheet" href="https://fonts.googleapis.com/css2?family=Source+Sans+3:wght@400;600;700&display=swap">
<style>
  :root {
    --backdrop: #2b2b2b;
    --card-top: #ffffff;
    --card-bottom: #d9d9d9;
    --panel-blue: #1f5a9e;
    --panel-blue-deep: #173f75;
    --gold: #e2b64a;
    --ink: #1c1c1c;
    --ink-soft: #3a3a3a;
    --dots: #8a8a8a;
    --white: #ffffff;
  }
  * { box-sizing: border-box; margin: 0; padding: 0; }
  html, body {
    width: 1200px; height: 968px; overflow: hidden;
    background: var(--backdrop);
    font-family: "Source Sans 3", "Myriad Pro", sans-serif;
  }
  .card {
    position: absolute; left: 410px; top: 34px;
    width: 380px; height: 900px;
    background: linear-gradient(180deg, var(--card-top) 0%, var(--card-top) 45%, var(--card-bottom) 100%);
  }
  .brand-panel {
    position: absolute; left: 30px; top: 0;
    width: 320px; height: 430px;
  }
  .brand-panel svg { position: absolute; inset: 0; }
  .skyline-art {
    position: absolute; left: 40px; top: 40px;
    width: 240px; height: 180px;
    background: linear-gradient(180deg, #2a6bb4 0%, #1d4f8e 100%);
    border-radius: 4px;
  }
  .brand-name {
    position: absolute; left: 0; right: 0; top: 236px;
    text-align: center; color: var(--white);
    font-weight: 700; font-size: 38px; letter-spacing: 1px;
  }
  .brand-name::before {
    content: ""; display: inline-block;
    width: 14px; height: 14px; background: var(--white);
    border-radius: 50%; margin-right: 10px; vertical-align: middle;
  }
  .brand-city {
    position: absolute; left: 0; right: 0; top: 290px;
    text-align: center; color: var(--white);
    font-weight: 400; font-size: 22px; letter-spacing: 2px;
  }
  .brand-address {
    position: absolute; left: 112px; top: 335px;
    color: var(--white); font-size: 12.5px; line-height: 1.4;
  }
  .contact {
    position: absolute; left: 0; right: 0; top: 448px;
    text-align: center; color: var(--ink);
  }
  .contact-name { font-weight: 700; font-size: 22px; line-height: 1.1; }
  .contact-title { font-size: 18px; color: var(--ink-soft); line-height: 1.2; }
  .rule-dotted {
    width: 170px; margin: 6px auto 8px;
    border-top: 3px dotted var(--ink);
  }
  .contact-lines { font-size: 17px; line-height: 1.3; }
  .foot-rule {
    position: absolute; left: 0; right: 0; bottom: 34px;
    border-top: 2px dotted var(--dots);
  }
  .foot-star {
    position: absolute; left: 50%; bottom: 25px;
    width: 18px; height: 18px; margin-left: -9px;
  }
</style>
</head>
<body>
  <main class="card">
    <section class="brand-panel">
      <svg viewBox="0 0 320 430" width="320" height="430" aria-hidden="true">
        <path d="M0,0 H320 V390 A40 40 0 0 0 280 430 H40 A40 40 0 0 0 0 390 Z" fill="var(--panel-blue)"/>
        <path d="M8,8 H312 V382.7 A48 48 0 0 0 272.7 422 H47.3 A48 48 0 0 0 8 382.7 Z" fill="none" stroke="var(--gold)" stroke-width="2"/>
      </svg>
      <div class="skyline-art" role="img" aria-label="Illustration of a city skyline with a glass of beer and wheat ears"></div>
      <div class="brand-name">Kestrel Beer</div>
      <div class="brand-city">New York</div>
      <address class="brand-address">
        42 Harlow Street<br>
        Brooklyn, NY 11206<br>
        Phone: (718) 555-0143
      </address>
    </section>

    <section class="contact">
      <div class="contact-name">Dan Okafor</div>
      <div class="contact-title">Sales Manager</div>
      <div class="rule-dotted"></div>
      <div class="contact-lines">
        Cell: (917) 555-0178<br>
        okafor@mailbox.com<br>
        www.kestrelbeerco.com
      </div>
    </section>

    <div class="foot-rule"></div>
    <svg class="foot-star" viewBox="0 0 20 20" aria-hidden="true">
      <polygon points="10,1 12.6,7.2 19.5,7.6 14.2,12 15.9,18.8 10,15 4.1,18.8 5.8,12 0.5,7.6 7.4,7.2" fill="var(--ink)"/>
    </svg>
  </main>
</body>
</html>
```